Hollerby Consulting needs a quality & professional business card!

I am a recruitment and employment consultant from Brisbane, Australia and I had a fantastic logo organised by this community to I am hoping the business card will be the same.

I have attached the Hollerby consulting logo that ideally would feature on the back of the business card. There are a number of logos for you to use as you see fit. I would like the colour cheme to match that of the Hollerby Consulting logo. I also have a secondary company called Career Lantern Australia and I have included that logo as well. While it is an important part of the business I don't want this logo feature too predominantly as I am moving out of this space. This logo was created by myself and is of low quality. Feel free to use the icon and words however you want. The winning design will be smart, professional and eye-catching.

The information I am looking for in the business card is:
Name: Derek Hollerby
Position: Founder & Director
Phone: (07) 3156 4082
Mobile: 0418 672 051
Email: derek@careerlantern-example.com.au

Target Market(s)

Recruiters, government, large companies

Contact Information for Business Card

Name: Derek Hollerby
Phone: (07) 3156 4082
Mobile: 0418 672 051
Web: www.careerlantern-example.com.au

Font styles to use
Serif
Sans Serif

Requirements
Must have
• Hollerby Consulting Logo on reverse side
• Contact details on front side with smaller reference to Hollerby Consulting logo and Career Lantern Australia logo

```html
<!DOCTYPE html>
<html lang="en">
<head>
<meta charset="utf-8">
<title>Hollerby Consulting – Business Card</title>
<link rel="stylesheet" href="https://fonts.googleapis.com/css2?family=Work+Sans:wght@400;500&display=swap">
<style>
  :root {
    --page-bg: #262626;
    --card-bg: #1c1c1c;
    --card-bg-light: #2a2a2a;
    --accent-blue: #1a92d6;
    --text-white: #f4f4f4;
    --text-grey: #9a9a9a;
  }
  * { box-sizing: border-box; margin: 0; padding: 0; }
  html, body {
    width: 1200px; height: 900px; overflow: hidden;
    background: var(--page-bg);
    font-family: "Work Sans", Arial, sans-serif;
  }
  .card {
    position: absolute;
    left: 250px;
    width: 700px; height: 390px;
    background: linear-gradient(135deg, var(--card-bg) 40%, var(--card-bg-light) 100%);
    border-bottom: 6px solid var(--accent-blue);
    box-shadow: 0 12px 30px rgba(0,0,0,0.45);
    overflow: hidden;
  }
  .card--back { top: 45px; }
  .card--front { top: 465px; }

  .brand-name {
    color: var(--text-white);
    font-weight: 500;
    text-transform: uppercase;
    letter-spacing: 0.08em;
    line-height: 1.05;
  }
  .card--back .brand-name {
    position: absolute; left: 0; right: 0; top: 150px;
    text-align: center; font-size: 44px;
  }
  .secondary-brand {
    position: absolute; right: 34px; bottom: 26px;
    color: var(--text-white); font-weight: 500; font-size: 20px;
  }

  .card--front .brand-name {
    position: absolute; left: 50px; top: 140px;
    font-size: 34px;
  }
  .divider {
    position: absolute; left: 352px; top: 110px;
    width: 2px; height: 130px; background: var(--accent-blue);
  }
  .contact {
    position: absolute; left: 380px; top: 110px;
    color: var(--text-white);
  }
  .contact__name {
    color: var(--accent-blue); font-weight: 500;
    font-size: 28px; text-transform: uppercase; line-height: 1;
  }
  .contact__role { font-size: 18px; margin: 6px 0 14px; letter-spacing: 0.03em; }
  .contact__list { list-style: none; font-size: 17px; }
  .contact__list li { display: flex; align-items: center; gap: 12px; height: 24px; letter-spacing: 0.04em; }
  .contact__list svg { width: 12px; height: 12px; flex: none; }
  .contact__list .email { font-size: 15px; }
</style>
</head>
<body>
  <section class="card card--back" aria-label="Card back">
    <p class="brand-name">Hollerby Consulting</p>
    <p class="secondary-brand">Career Lantern Australia</p>
  </section>

  <section class="card card--front" aria-label="Card front">
    <p class="brand-name">Hollerby<br>Consulting</p>
    <div class="divider"></div>
    <div class="contact">
      <h1 class="contact__name">Derek Hollerby</h1>
      <p class="contact__role">Founder &amp; Director</p>
      <ul class="contact__list">
        <li>
          <svg viewBox="0 0 12 12" aria-hidden="true"><rect x="3" y="0.5" width="6" height="11" rx="1" fill="none" stroke="var(--accent-blue)" stroke-width="1.2"/><line x1="5" y1="9.5" x2="7" y2="9.5" stroke="var(--accent-blue)"/></svg>
          (07) 3156 4082
        </li>
        <li>
          <svg viewBox="0 0 12 12" aria-hidden="true"><path d="M2.5 1 L4.5 1 L5.3 3.6 L4 4.6 Q5 7 7.4 8 L8.4 6.7 L11 7.5 L11 9.5 Q11 11 9.5 11 Q1 10 1 2.5 Q1 1 2.5 1 Z" fill="var(--accent-blue)"/></svg>
          0418 672 051
        </li>
        <li class="email">
          <svg viewBox="0 0 12 12" aria-hidden="true"><rect x="0.6" y="2" width="10.8" height="8" fill="none" stroke="var(--accent-blue)" stroke-width="1.2"/><polyline points="0.6,2 6,6.5 11.4,2" fill="none" stroke="var(--accent-blue)" stroke-width="1.2"/></svg>
          derek@careerlantern-example.com.au
        </li>
      </ul>
    </div>
  </section>
</body>
</html>
```